Need Primer (paint) Label Design

THE ATTACHED LABEL/S ARE SOLEY FOR REFERENCE. DO NOT MAKE ME AN INTERIOR PAINT OR CHALK PAINT LABEL. I ONLY NEED A "PRIMER" LABEL. THE ATTACHED INTERIOR PAINT LABEL IS ONLY TO SHOW YOU THE THEME/DESIGN OF OUR OTHER LABELS. THE BLUE LABEL ONLY HAS A DESIGN ASPECT I LIKE (PRIMER ON SIDE). The last four labels are our competitors.
```````````````````````````````````````````````````````````````````````````````````````````````````
We need this label to look professional, sharp, eye catching and modern.
OUR PRIMARY COLORS ARE BLACK AND WHITE. IF YOU INCOPORATE ANOTHER COLOR, SILVER OR GOLD MIGHT BE IDEAL BUT PLEASE DON'T DRIFT TOO FAR.
The attached documents:
1st - Our Logo
2nd - Our chalk paint label (reference). We do not need a chalk paint label.
3rd. A random design example. I like the PRIME on the side running vertically. I think it's a cool design concept.
````````````````````````````````````````````````````````````````````````````````````````````````````
We are going to be using a normal paint can with a metal bail/handle so please use that with you design work
``````````````````````````````````````````````````````````````````````````````````````````````````
Order, in my head:
2743
Coatings
^^ I want this to stand out as well but I don't want it to be the first thing your eye is drawn to. Probably 2nd
Interior/Exterior
Multi - Surface Primer
^^ Want this to stick out and draw your eye so the customer knows what it is immediately
Exceptional Adhesion, Performance, Durability,
Use on Wood, Drywall, Plaster, Stucco, Masonry, Brick, Paneling, Painted Metal, & Properly Prepared Glossy Surfaces & More
35* Lowe Temperature Application (can be on side or small)
100% Acrylic
Low Odor - Low VOC - Soap & Water Clean Up
1 US Gallon - 3.785 L
Feel free to get creative with it!

```html
<!DOCTYPE html>
<html lang="en">
<head>
<meta charset="utf-8">
<title>2743 Coatings — Multi-Surface Primer Label</title>
<link rel="stylesheet" href="https://fonts.googleapis.com/css2?family=Montserrat:wght@400;500;700;800;900&display=swap">
<style>
  :root {
    --ink: #0b0b0b;
    --paper: #ffffff;
    --stage: #f4f4f4;
    --gold-deep: #6e4f21;
    --gold: #b8904f;
    --gold-light: #e6cf9a;
    --dot: #d1ad69;
  }
  html, body {
    margin: 0;
    padding: 0;
    width: 710px;
    height: 1200px;
    overflow: hidden;
    background: var(--stage);
  }
  .stage {
    position: relative;
    width: 710px;
    height: 1200px;
  }
  .label {
    position: absolute;
    left: 30px;
    top: 292px;
    width: 650px;
    height: 615px;
    box-shadow: 6px 8px 10px rgba(0, 0, 0, 0.28);
    background: var(--paper);
  }
  .label svg { display: block; width: 100%; height: 100%; }
  .brand { font-family: "Montserrat", sans-serif; font-weight: 500; fill: var(--paper); }
  .head { font-family: "Montserrat", sans-serif; font-weight: 800; fill: var(--paper); }
  .claim { font-family: "Montserrat", sans-serif; font-weight: 800; fill: var(--paper); font-size: 17px; text-anchor: middle; }
  .benefits { font-family: "Montserrat", sans-serif; font-weight: 700; fill: var(--paper); font-size: 18.5px; }
  .surfaces { font-family: "Montserrat", sans-serif; font-weight: 400; fill: var(--paper); font-size: 14.5px; }
  .spec { font-family: "Montserrat", sans-serif; fill: var(--ink); text-anchor: middle; }
  .spec-big { font-weight: 900; }
  .spec-bold { font-weight: 800; }
  .spec-light { font-weight: 400; }
  .product-type { font-family: "Montserrat", sans-serif; font-weight: 800; fill: var(--ink); }
  .product-name { font-family: "Montserrat", sans-serif; font-weight: 900; fill: var(--ink); }
</style>
</head>
<body>
<main class="stage">
  <section class="label" aria-label="2743 Coatings Multi-Surface Primer label">
    <svg viewBox="0 0 888 840" xmlns="http://www.w3.org/2000/svg">
      <defs>
        <linearGradient id="goldEdge" x1="0" y1="0" x2="0" y2="1">
          <stop offset="0" stop-color="var(--gold-deep)"/>
          <stop offset="0.6" stop-color="var(--gold)"/>
          <stop offset="1" stop-color="var(--gold-light)"/>
        </linearGradient>
        <linearGradient id="goldBand" x1="0" y1="0" x2="1" y2="0">
          <stop offset="0" stop-color="var(--gold-deep)"/>
          <stop offset="0.4" stop-color="var(--gold)"/>
          <stop offset="1" stop-color="var(--gold-light)"/>
        </linearGradient>
        <linearGradient id="goldRule" x1="0" y1="0" x2="1" y2="0">
          <stop offset="0" stop-color="var(--gold-deep)"/>
          <stop offset="0.5" stop-color="var(--gold)"/>
          <stop offset="1" stop-color="var(--gold-deep)"/>
        </linearGradient>
      </defs>

      <!-- gold edge behind the black panel -->
      <path class="panel-edge" d="M0 0 H676 L586 520 C563 648 506 702 402 702 L0 702 Z" fill="url(#goldEdge)"/>
      <path class="panel-band" d="M0 690 H402 L402 702 H0 Z" fill="url(#goldBand)"/>
      <!-- black panel -->
      <path class="panel" d="M0 0 H665 L576 518 C554 640 500 690 402 690 L0 690 Z" fill="var(--ink)"/>

      <!-- brand -->
      <text class="brand" x="75" y="275" font-size="290" textLength="465" lengthAdjust="spacingAndGlyphs">2743</text>
      <text class="brand" x="75" y="368" font-size="78" textLength="465" lengthAdjust="spacingAndGlyphs">COATINGS</text>

      <!-- category -->
      <rect x="75" y="408" width="463" height="2.5" fill="url(#goldRule)"/>
      <text class="head" x="71" y="462" font-size="43" textLength="466" lengthAdjust="spacingAndGlyphs">INTERIOR/EXTERIOR</text>
      <rect x="75" y="478" width="463" height="2.5" fill="url(#goldRule)"/>

      <!-- claims -->
      <text class="claim" x="134" y="508">EXCEPTIONAL</text>
      <text class="claim" x="134" y="526">ADHESION</text>
      <rect x="219" y="483" width="2" height="47" fill="var(--gold)"/>
      <text class="claim" x="312" y="518">PERFORMANCE</text>
      <rect x="401" y="483" width="2" height="47" fill="var(--gold)"/>
      <text class="claim" x="475" y="518">DURABILITY</text>

      <text class="benefits" x="65" y="574" textLength="474" lengthAdjust="spacingAndGlyphs">LOW ODOR - LOW VOC - SOAP &amp; WATER CLEAN UP</text>
      <text class="surfaces" x="66" y="607">USE ON WOOD  ·  DRYWALL  ·  PLASTER  ·  STUCCO  ·</text>
      <text class="surfaces" x="66" y="627">MASONRY  ·  BRICK  ·  PANELING  ·  PAINTED METAL  ·</text>
      <text class="surfaces" x="66" y="647">&amp; PROPERLY PREPARED GLOSSY SURFACES &amp; MORE</text>

      <!-- bottom specs -->
      <text class="spec spec-big" x="140" y="752" font-size="54">35*</text>
      <text class="spec spec-bold" x="140" y="779" font-size="12.5">LOWE TEMPERATURE</text>
      <text class="spec spec-bold" x="140" y="792" font-size="12.5">APPLICATION</text>
      <rect x="229" y="720" width="2" height="78" fill="var(--gold)"/>
      <text class="spec spec-bold" x="343" y="767" font-size="26">1 US GALLON</text>
      <text class="spec spec-bold" x="343" y="794" font-size="26">3.785 L</text>
      <rect x="452" y="720" width="2" height="78" fill="var(--gold)"/>
      <text class="spec spec-big" x="550" y="762" font-size="52" textLength="144" lengthAdjust="spacingAndGlyphs">100%</text>
      <text class="spec spec-light" x="550" y="797" font-size="33" textLength="146" lengthAdjust="spacingAndGlyphs">ACRYLIC</text>

      <!-- vertical product name -->
      <text class="product-type" transform="translate(711 492) rotate(-90)" font-size="46" textLength="402" lengthAdjust="spacingAndGlyphs">MULTI - SURFACE</text>
      <text class="product-name" transform="translate(842 792) rotate(-90)" font-size="205" textLength="726" lengthAdjust="spacingAndGlyphs">Prımer</text>
      <circle class="i-dot" cx="690" cy="532" r="25" fill="var(--dot)"/>
    </svg>
  </section>
</main>
</body>
</html>
```